依頼詳細
最近、全国高校用教科書を編集しています。この度、これに対応した『テキスト』を関連編集しています。全部で16 unitありますが、設問のパターンはほとんど同じものです。ですから、『unit1』を対象に、6ページの基本編集レイアウトの作成を依頼したいのです。よろしくお願いします。
記載項目
『unit1』の原稿は添付いたします。
希望イメージ
シンプル 複雑
単色 カラフル
暗い 明るい
日常 高級
遊び心 厳粛
未来的 伝統的
女性的 男性的
希望する色
納品ファイル
• 高解像度JPG (.jpg)
• イラストレーター形式 (.ai)
補足説明
■ 選んだ理由

全ページのバランスが最もとれており、見本ページにふさわしかったので、本提案を当選として選びました。

■ 提案者全員のお礼・コメント

お盆休みの中、たくさんの御提案をいただきまして、大変感謝しております。当社は出版社ですから、依頼事項が続きます。今後とも、よろしくお願い申し上げます。

```html
<!DOCTYPE html>
<html lang="ja">
<head>
<meta charset="utf-8">
<link href="https://fonts.googleapis.com/css2?family=Noto+Sans+JP:wght@400;700&family=Noto+Serif+JP:wght@400&family=Roboto+Slab:wght@700;800&display=swap" rel="stylesheet">
<style>
:root{--ink:#222;--soft:#555;--rule:#999;--frame:#d6d6d6;--accent:#c8102e;--bg:#fff;--cell:#f2f2f2}
*{box-sizing:border-box;margin:0;padding:0}
html,body{width:1200px;height:581px;overflow:hidden;background:var(--bg)}
body{position:relative;font-family:"Noto Serif JP",serif;color:var(--ink)}
.page{position:absolute;top:28px;width:296px;height:415px;border:1px solid var(--frame);background:#fff;overflow:hidden}
.p1{left:22px}.p2{left:342px}.p3{left:662px}
.unit-head{position:absolute;top:10px;right:12px;display:flex;align-items:center;gap:3px;font-family:"Roboto Slab",serif;font-size:6.5px;font-weight:700;white-space:nowrap}
.unit-tag{background:var(--accent);color:#fff;font-size:4.5px;padding:1px 3px}
.unit-head small{font-family:"Noto Sans JP",sans-serif;font-weight:400;font-size:3.5px;color:var(--soft)}
.sec-head{position:absolute;top:24px;left:12px;right:12px;height:14px;border-bottom:.6px solid var(--rule);display:flex;align-items:flex-end;gap:4px;padding-bottom:1px;white-space:nowrap}
.sec-num{font-family:"Roboto Slab",serif;font-size:5px;font-weight:700}
.sec-title{font-family:"Roboto Slab",serif;font-size:10px;font-weight:800;line-height:1}
.sec-title small{font-size:5px}
.stars{font-size:3.5px;letter-spacing:.3px;margin-left:6px}
.grade{margin-left:auto;font-family:"Noto Sans JP",sans-serif;font-size:3.5px;display:flex;gap:5px;align-items:center;border-left:.6px solid var(--rule);padding-left:4px}
.grade b{font-size:6px;font-weight:400}
.foot{position:absolute;left:12px;right:12px;bottom:12px;height:3px;border-top:1.2px solid var(--ink);border-bottom:.5px solid var(--ink)}
.body{position:absolute;left:16px;right:14px;font-size:4px;line-height:1.55}
.label{display:inline-block;background:var(--ink);color:#fff;font-family:"Roboto Slab",serif;font-weight:700;font-size:7px;width:10px;height:10px;text-align:center;line-height:10px;position:absolute;left:-4px}
.indent{padding-left:14px}
table{border-collapse:collapse;margin:4px 0 4px 14px;width:200px;font-size:3.6px}
td{border:.4px solid var(--rule);padding:.6px 3px}
td:first-child{background:var(--cell);width:42%}
.line{border-bottom:.4px solid var(--rule);height:5px;margin:1px 0 3px 10px}
.q{display:flex;justify-content:space-between;gap:4px}
.sq{font-family:"Noto Sans JP",sans-serif;font-weight:700;font-size:4px}
</style>
</head>
<body>

<section class="page p1">
  <div class="unit-head"><span class="unit-tag">Unit 1</span>Ken, This Is Oliver<small>Step Ahead</small></div>
  <header class="sec-head"><span class="sec-num">04.</span><span class="sec-title">Jump</span><span class="stars">★★★★★</span></header>
  <div class="body" style="top:52px">
    <span class="label">A</span>
    <div class="indent">【紹介する】 あなたは、フィリピンからの留学生Emilyのホストファミリーです。<br>Emilyをクラスメートに紹介してみましょう。3人1組になって、順番にロールプレイをしましょう。<br>Emilyの情報は下記の情報を参考にしましょう。</div>
    <table>
      <tr><td>Name</td><td>Emily Grant</td></tr>
      <tr><td>From</td><td>The Philippines</td></tr>
      <tr><td>Languages</td><td>Tagalog, English</td></tr>
      <tr><td>Reason why she came to Japan</td><td>To study art</td></tr>
      <tr><td>Hobby</td><td>Watch movies, cook, write in her diary</td></tr>
      <tr><td>Favorite places in Japan</td><td>Nagasaki and Kyoto</td></tr>
      <tr><td>Future career</td><td>Art teacher</td></tr>
    </table>
    <div class="indent">e.g.)<br>A: Hi, Naomi. This is Emily.<br>&nbsp;&nbsp;&nbsp;She's from the Philippines and she is doing a home-stay at my place.<br>B: Hi, Emily, I'm Naomi. Nice to meet you. Why did you come to Japan?<br>C: Well, I'm still a student and I'm here to study…<br>&nbsp;&nbsp;&nbsp;&nbsp;&nbsp;&nbsp;&nbsp;&nbsp;&nbsp;&nbsp;&nbsp;&nbsp;&nbsp;&nbsp;&nbsp;&nbsp;&nbsp;&nbsp;&nbsp;&nbsp;&nbsp;&nbsp;&nbsp;&nbsp;&nbsp;&nbsp;（中略）<br>C: It was really fun talking to you, Naomi.<br>B: Yes, I really enjoyed meeting you, Emily.</div>
  </div>
  <div class="body" style="top:276px">
    <span class="label">B</span>
    <div class="indent">【紹介する】 あなたの友達をクラスで紹介してみましょう。<br>STEP Bで作成した表を参照しながら原稿を書き、プレゼンテーションの練習をしましょう。<br><br>e.g.)<br>Hi, everyone. Today I want to talk about Yuna, a friend I've known for years.<br>Actually, we first met in kindergarten and we have been close ever since...<br>Thanks very much for listening.</div>
  </div>
  <div class="foot"></div>
</section>

<section class="page p2">
  <div class="unit-head"><span class="unit-tag">Unit 1</span>Ken, This Is Oliver<small>Step Ahead</small></div>
  <header class="sec-head"><span class="sec-num">05.</span><span class="sec-title">Vocabulary <small>(Basic)</small></span><span class="stars">★★★★★</span><span class="grade">評価 <b>A</b><b>B</b><b>C</b></span></header>
  <div class="body" style="top:44px;left:12px">
    <div class="sq">【1】 <span style="font-weight:400">次の各文を日本語に訳し、SV, SVC, SVO, SVOO, SVOC などの文型を答えなさい。</span></div>
    <div class="indent">① She smelled the lilies.<div class="q"><span>(</span><span>)[&nbsp;&nbsp;&nbsp;&nbsp;&nbsp;&nbsp;&nbsp;&nbsp;&nbsp;]</span></div>
    ② Tom showed his diary to his wife.<div class="q"><span>(</span><span>)[&nbsp;&nbsp;&nbsp;&nbsp;&nbsp;&nbsp;&nbsp;&nbsp;&nbsp;]</span></div>
    ③ Mary bought her mother a rose.<div class="q"><span>(</span><span>)[&nbsp;&nbsp;&nbsp;&nbsp;&nbsp;&nbsp;&nbsp;&nbsp;&nbsp;]</span></div>
    ④ Tom lives in Tokyo.<div class="q"><span>(</span><span>)[&nbsp;&nbsp;&nbsp;&nbsp;&nbsp;&nbsp;&nbsp;&nbsp;&nbsp;]</span></div>
    ⑤ That sounds like a great idea.<div class="q"><span>(</span><span>)[&nbsp;&nbsp;&nbsp;&nbsp;&nbsp;&nbsp;&nbsp;&nbsp;&nbsp;]</span></div></div>
    <div class="sq" style="margin-top:3px">【2】 <span style="font-weight:400">(　　　)内から適切な語句を選びなさい。</span></div>
    <div class="indent">① I totally ( agree / agree with / agree in ) you.<br>② Have you ( heard / heard from / heard with ) Tom lately?<br>③ He ( looked / looked at / looked on ) me.<br>④ His remark ( let / made / did ) me angry.</div>
    <div class="sq" style="margin-top:3px">【3】 <span style="font-weight:400">日本語に合うように、(　　　)に適切な語句を入れなさい。</span></div>
    <div class="indent">① 先生は私たちのことをよく面倒をみてくれる。<br>&nbsp;&nbsp;Our teacher looks(　　　　　　　　) us well.<br>② 私たちは試合に勝つのは難しいことがわかった。<br>&nbsp;&nbsp;We(　　　　　) it difficult to(　　　　　) the game.<br>③ 先生はその生徒に教室を出るように言った。<br>&nbsp;&nbsp;The teacher(　　　　　) the student(　　　　　) leave the classroom.<br>④ 彼は英語を勉強するのを楽しんでいます。<br>&nbsp;&nbsp;He(　　　　　) studying English.<br>⑤ 彼がパーティ会場にやっと到着した。<br>&nbsp;&nbsp;He finally(　　　　　　) at the party place.</div>
    <div class="sq" style="margin-top:3px">【4】 <span style="font-weight:400">日本語に合うように、(　　　)内の語句を並べかえなさい。</span></div>
    <div class="indent">
      <div class="q"><span>① 彼女はパーティを楽しんだ。</span><span>She ( herself / enjoyed / the party / at ).</span></div><div class="line"></div>
      <div class="q"><span>② 私たちは他のことをほっておいた。</span><span>( left / alone / him / we ).</span></div><div class="line"></div>
      <div class="q"><span>③ 彼は私たちにそこへの行き方を教えてくれた。</span><span>He ( to / how / us / showed / there / get ).</span></div><div class="line"></div>
      <div class="q"><span>④ 皆、最初は少し緊張しているように見えた。</span><span>Everybody ( at first / nervous / a little / looked ).</span></div><div class="line"></div>
      <div class="q"><span>⑤ 近所で大きな火事が発生した。</span><span>There ( a / fire / neighborhood / big / was / in / the ).</span></div><div class="line"></div>
    </div>
  </div>
  <div class="foot"></div>
</section>

<section class="page p3">
  <div class="unit-head"><span class="unit-tag">Unit 1</span>Ken, This Is Oliver<small>Step Ahead</small></div>
  <header class="sec-head"><span class="sec-num">06.</span><span class="sec-title">Vocabulary <small>(Practice)</small></span><span class="stars">★★★★★</span><span class="grade">評価 <b>A</b><b>B</b><b>C</b></span></header>
  <div class="body" style="top:46px;left:14px;line-height:2">
    次の表現を参考にして、自己紹介文を英語で書き、クラスの皆に伝えましょう。<br><br>
    ･I'd like to introduce myself.<br>
    ･My favorite subject is(　　　　　　　　　).<br>
    ･My family is large (small).<br>
    ･I have a pet dog (cat) named(　　　　　　　　　).<br>
    ･My father works for(　　　　　　　　) and my mother ~.<br>
    ･I dream of being ~.
  </div>
  <div class="foot"></div>
</section>

</body>
</html>
```